Thermostat Screen Design

We need a screen layout design for a new thermostat we're currently developing. If you're not familiar with thermostats, you can see some examples here - http://smart-climate-units-guide.bestpickdigest.com/

We're after the main page design, with icons, colours etc. It needs to be clean, modern and minimalistic. Attached is all components required on the screen. The screen size is 5 inch (diagnol).

The arrows on the screen showcase what happens when you press a button. For example, when you press MODE once you get OFF, press it twice, HEAT, press it 3 times, COOL, etc. This is just for your reference.

You have complete creative license on how you choose to layout the screen, position the components etc, but we require:

- it must be on a 5 inch screen diagnol
- modern, clean and minimalistic
- includes icons and colours
- Intuitive

Let me know if any questions.

```html
<!DOCTYPE html>
<html lang="en">
<head>
<meta charset="utf-8">
<title>Thermostat Screen Design</title>
<link rel="stylesheet" href="https://fonts.googleapis.com/css2?family=Arimo:wght@400;700&display=swap">
<style>
  :root {
    --backdrop: #000000;
    --sheet: #ffffff;
    --ink: #111111;
    --ink-soft: #333333;
    --white: #ffffff;
    --blue: #12a6dc;
    --blue-deep: #0a7eae;
    --blue-light: #1cbce8;
    --blue-text: #0b8db7;
    --red: #e21a1c;
    --red-deep: #a80f10;
    --red-light: #ee2a22;
    --red-text: #bf1217;
  }
  * { box-sizing: border-box; margin: 0; padding: 0; }
  html, body { width: 1200px; height: 900px; overflow: hidden; }
  body {
    background: var(--backdrop);
    font-family: "Arimo", Arial, sans-serif;
    position: relative;
  }
  .sheet { position: absolute; left: 224px; width: 780px; background: var(--sheet); }
  .sheet--top { top: 0; height: 445px; }
  .sheet--bottom { top: 452px; height: 448px; }

  .screen { position: absolute; left: 224px; width: 780px; height: 445px; }
  .screen--cool { top: 0; --tone: var(--blue); --tone-deep: var(--blue-deep); --tone-light: var(--blue-light); --tone-text: var(--blue-text); }
  .screen--warm { top: 442px; --tone: var(--red); --tone-deep: var(--red-deep); --tone-light: var(--red-light); --tone-text: var(--red-text); }

  .nav-button {
    position: absolute; left: 42px; width: 83px; height: 83px;
    background: var(--tone); border-radius: 5px; color: var(--white);
    display: flex; flex-direction: column; align-items: center;
    padding-top: 8px; font-weight: 700; font-size: 14px;
  }
  .nav-button svg { margin-top: 6px; }
  .nav-button--mode { top: 42px; background: var(--tone-deep); }
  .nav-button--fan { top: 138px; }
  .nav-button--zone { top: 234px; }
  .nav-button--settings { top: 331px; }

  .pill {
    position: absolute; background: var(--tone); color: var(--white);
    font-weight: 700; border-radius: 6px;
    display: flex; align-items: center; justify-content: center;
  }
  .pill--date { left: 195px; top: 34px; width: 285px; height: 44px; font-size: 22px; }
  .pill--sleep { left: 543px; top: 41px; width: 88px; height: 32px; font-size: 19px; }
  .pill--zone { left: 641px; top: 41px; width: 97px; height: 32px; font-size: 19px; }
  .pill--time { left: 585px; top: 131px; width: 111px; height: 34px; font-size: 20px; }

  .climate-card {
    position: absolute; left: 154px; top: 130px; width: 366px; height: 292px;
    border-radius: 52px;
    background: radial-gradient(circle at 60% 35%, var(--tone-light), var(--tone) 75%);
  }
  .reading {
    position: absolute; top: 19px; height: 39px; background: var(--white);
    text-align: center; color: var(--ink-soft);
  }
  .reading__label { font-size: 13px; margin-top: 2px; }
  .reading--outdoor { left: 50px; width: 87px; }
  .reading--outdoor .reading__value { font-size: 23px; color: var(--tone-text); line-height: 22px; }
  .reading--humidity { left: 144px; width: 175px; }
  .reading--humidity .reading__value { font-size: 20px; font-weight: 700; color: var(--tone-text); line-height: 22px; }

  .room-panel {
    position: absolute; left: 30px; top: 93px; width: 165px; height: 161px;
    background: var(--white); border-radius: 20px; text-align: center;
  }
  .room-panel__title { font-size: 23px; color: var(--ink-soft); margin-top: 11px; }
  .room-panel__temp { font-size: 68px; font-weight: 700; color: var(--tone-text); line-height: 64px; margin-top: 2px; }
  .room-panel__status {
    position: absolute; left: 29px; bottom: 10px; text-align: left;
    font-size: 12px; font-weight: 700; color: var(--ink); line-height: 15px;
  }
  .room-panel__status span { color: var(--tone-text); }

  .mode-pill {
    position: absolute; width: 87px; height: 22px; background: var(--white);
    border-radius: 11px; font-size: 18px; font-weight: 700; color: var(--ink);
    display: flex; align-items: center; justify-content: center;
  }
  .mode-pill--heat { left: 206px; top: 116px; }
  .mode-pill--cool { left: 208px; top: 210px; width: 84px; }

  .setpoint {
    position: absolute; left: 219px; top: 147px; width: 63px; height: 54px;
    background: var(--white); text-align: center;
  }
  .setpoint__label { font-size: 13px; color: var(--ink-soft); margin-top: 3px; }
  .setpoint__value { font-size: 29px; font-weight: 700; color: var(--tone-text); line-height: 30px; }

  .step { position: absolute; left: 303px; }
  .step--up { top: 116px; }
  .step--down { top: 207px; }
</style>
</head>
<body>
  <div class="sheet sheet--top"></div>
  <div class="sheet sheet--bottom"></div>

  <section class="screen screen--cool">
    <div class="nav-button nav-button--mode">MODE
      <svg width="46" height="46" viewBox="0 0 46 46"><path d="M38 16 A17 17 0 1 0 40 25" fill="none" stroke="#fff" stroke-width="4"/><polygon points="31,26 44,22 41,36" fill="#fff"/></svg>
    </div>
    <div class="nav-button nav-button--fan">FAN
      <svg width="46" height="46" viewBox="0 0 46 46"><g fill="#fff"><path d="M21 20 C16 10 2 10 4 20 C5 26 14 26 21 23Z"/><path d="M25 20 C32 14 42 6 44 14 C45 22 34 24 25 24Z"/><path d="M22 26 C20 34 22 44 29 44 C36 43 32 32 26 26Z"/><circle cx="23" cy="23" r="5"/></g><circle cx="23" cy="23" r="2" fill="var(--tone)"/></svg>
    </div>
    <div class="nav-button nav-button--zone">ZONE
      <svg width="46" height="46" viewBox="0 0 46 46"><rect x="6" y="5" width="34" height="36" fill="none" stroke="#fff" stroke-width="3.5" stroke-dasharray="6 4"/></svg>
    </div>
    <div class="nav-button nav-button--settings">SETTINGS
      <svg width="50" height="50" viewBox="0 0 50 50"><g fill="#fff"><circle cx="25" cy="25" r="16"/><g id="teeth-c"><rect x="20" y="4" width="10" height="10"/><rect x="20" y="36" width="10" height="10"/><rect x="4" y="20" width="10" height="10"/><rect x="36" y="20" width="10" height="10"/></g><use href="#teeth-c" transform="rotate(45 25 25)"/></g><circle cx="25" cy="25" r="10" fill="var(--tone)"/></svg>
    </div>

    <div class="pill pill--date">Sunday, March-17-2014</div>
    <div class="pill pill--sleep">SLEEP</div>
    <div class="pill pill--zone">ZONE 1</div>
    <div class="pill pill--time">08:35 PM</div>

    <div class="climate-card">
      <div class="reading reading--outdoor"><div class="reading__label">OUTDOOR</div><div class="reading__value">22°</div></div>
      <div class="reading reading--humidity"><div class="reading__label">INDOOR RH</div><div class="reading__value">45% Humidity</div></div>
      <div class="room-panel">
        <div class="room-panel__title">ROOM</div>
        <div class="room-panel__temp">18°</div>
        <div class="room-panel__status">SLEEEP : <span>60 MIN</span><br>MODE &nbsp;&nbsp;: <span>AUTO</span></div>
      </div>
      <div class="mode-pill mode-pill--heat">HEAT</div>
      <div class="setpoint"><div class="setpoint__label">SET TO</div><div class="setpoint__value">21°</div></div>
      <div class="mode-pill mode-pill--cool">COOL</div>
      <svg class="step step--up" width="37" height="27" viewBox="0 0 37 27"><polygon points="18.5,0 37,27 0,27" fill="#000"/></svg>
      <svg class="step step--down" width="37" height="27" viewBox="0 0 37 27"><polygon points="0,0 37,0 18.5,27" fill="#fff"/></svg>
    </div>
  </section>

  <section class="screen screen--warm">
    <div class="nav-button nav-button--mode">MODE
      <svg width="46" height="46" viewBox="0 0 46 46"><path d="M38 16 A17 17 0 1 0 40 25" fill="none" stroke="#fff" stroke-width="4"/><polygon points="31,26 44,22 41,36" fill="#fff"/></svg>
    </div>
    <div class="nav-button nav-button--fan">FAN
      <svg width="46" height="46" viewBox="0 0 46 46"><g fill="#fff"><path d="M21 20 C16 10 2 10 4 20 C5 26 14 26 21 23Z"/><path d="M25 20 C32 14 42 6 44 14 C45 22 34 24 25 24Z"/><path d="M22 26 C20 34 22 44 29 44 C36 43 32 32 26 26Z"/><circle cx="23" cy="23" r="5"/></g><circle cx="23" cy="23" r="2" fill="var(--tone)"/></svg>
    </div>
    <div class="nav-button nav-button--zone">ZONE
      <svg width="46" height="46" viewBox="0 0 46 46"><rect x="6" y="5" width="34" height="36" fill="none" stroke="#fff" stroke-width="3.5" stroke-dasharray="6 4"/></svg>
    </div>
    <div class="nav-button nav-button--settings">SETTINGS
      <svg width="50" height="50" viewBox="0 0 50 50"><g fill="#fff"><circle cx="25" cy="25" r="16"/><g id="teeth-w"><rect x="20" y="4" width="10" height="10"/><rect x="20" y="36" width="10" height="10"/><rect x="4" y="20" width="10" height="10"/><rect x="36" y="20" width="10" height="10"/></g><use href="#teeth-w" transform="rotate(45 25 25)"/></g><circle cx="25" cy="25" r="10" fill="var(--tone)"/></svg>
    </div>

    <div class="pill pill--date">Sunday, March-17-2014</div>
    <div class="pill pill--sleep">SLEEP</div>
    <div class="pill pill--zone">ZONE 1</div>
    <div class="pill pill--time">08:35 PM</div>

    <div class="climate-card">
      <div class="reading reading--outdoor"><div class="reading__label">OUTDOOR</div><div class="reading__value">22°</div></div>
      <div class="reading reading--humidity"><div class="reading__label">INDOOR RH</div><div class="reading__value">45% Humidity</div></div>
      <div class="room-panel">
        <div class="room-panel__title">ROOM</div>
        <div class="room-panel__temp">18°</div>
        <div class="room-panel__status">SLEEEP : <span>60 MIN</span><br>MODE &nbsp;&nbsp;: <span>AUTO</span></div>
      </div>
      <div class="mode-pill mode-pill--heat">HEAT</div>
      <div class="setpoint"><div class="setpoint__label">SET TO</div><div class="setpoint__value">21°</div></div>
      <div class="mode-pill mode-pill--cool">COOL</div>
      <svg class="step step--up" width="37" height="27" viewBox="0 0 37 27"><polygon points="18.5,0 37,27 0,27" fill="#000"/></svg>
      <svg class="step step--down" width="37" height="27" viewBox="0 0 37 27"><polygon points="0,0 37,0 18.5,27" fill="#fff"/></svg>
    </div>
  </section>
</body>
</html>
```